RW Frameworks Inc Business cards

We need business cards using our existing logo but slightly modified. Right now the logo says RW Framework Masonry. We want to keep the RW part of the design, but replace the Framework Masonry portion with "FRAMEWORKS". Please see the attached file.
Ideally this would be a blank template so we can add Different Names, titles, and phone numbers later.
On the one side we want only the logo and on the other side the detail. I'm attaching an example for you to see.
Please reach out with any other questions. Our address and other details will be given out once we find a design we like.

Target Market(s)

Construction Industry

```html
<!DOCTYPE html>
<html lang="en">
<head>
<meta charset="utf-8">
<title>RW Frameworks Inc – Business Cards</title>
<link rel="stylesheet" href="https://fonts.googleapis.com/css2?family=Roboto:wght@400;500;700&display=swap">
<style>
  :root {
    --page: #e6e8eb;
    --blue: #1f83d8;
    --blue-deep: #1566b4;
    --blue-logo: #1d6fbf;
    --silver-light: #f7f7f8;
    --silver: #d9dbde;
    --grey-strip: #8d9096;
    --ink: #15181c;
    --logo-grey: #d3d6da;
    --chip: #a9acb1;
  }
  * { box-sizing: border-box; margin: 0; padding: 0; }
  html, body { width: 1200px; height: 1200px; overflow: hidden; }
  body {
    background: var(--page);
    font-family: "Roboto", Arial, sans-serif;
    position: relative;
  }
  .card {
    position: absolute;
    width: 500px;
    height: 310px;
    border-radius: 0 22px 22px 22px;
    overflow: hidden;
    box-shadow: 0 6px 18px rgba(0,0,0,.22);
  }
  .card--front-a { left: 110px; top: 296px; border-radius: 22px 0 22px 0; }
  .card--back-a  { left: 622px; top: 296px; }
  .card--front-b { left: 106px; top: 716px; border-radius: 22px 0 22px 0; }
  .card--back-b  { left: 616px; top: 716px; }

  /* front */
  .front__brand {
    position: absolute; left: 0; top: 0; width: 215px; height: 100%;
    background: linear-gradient(90deg, var(--silver) 0%, var(--silver-light) 70%);
  }
  .front__detail {
    position: absolute; left: 215px; top: 0; right: 0; height: 100%;
    background: var(--blue);
  }
  .front__strip {
    position: absolute; left: 0; right: 0; bottom: 0; height: 12px;
    background: var(--grey-strip);
  }
  .brand { position: absolute; left: 0; width: 215px; top: 66px; text-align: center; }
  .brand__mark {
    font-weight: 700; font-size: 64px; line-height: 1; letter-spacing: 2px;
    color: var(--blue-logo);
  }
  .brand__word {
    font-size: 11px; letter-spacing: 6.5px; color: var(--blue-logo); margin-top: 4px;
  }
  .brand__url { font-size: 9.5px; color: var(--blue-deep); margin-top: 4px; font-weight: 500; }
  .social { position: absolute; left: 56px; bottom: 40px; display: flex; gap: 14px; }
  .social__chip { width: 24px; height: 24px; border-radius: 4px; background: var(--chip); }

  .person { position: absolute; left: 38px; top: 72px; }
  .person__name { font-size: 22px; font-weight: 500; color: var(--ink); letter-spacing: .3px; }
  .person__role {
    display: flex; align-items: center; gap: 4px; margin-top: 2px;
    font-size: 16px; color: var(--ink);
  }
  .person__rule { width: 140px; height: 2px; background: var(--ink); }
  .contacts { position: absolute; left: 42px; top: 158px; list-style: none; }
  .contacts li {
    display: flex; align-items: center; gap: 10px;
    font-size: 10px; color: var(--ink); height: 16px;
  }
  .contacts .dot {
    width: 10px; height: 10px; border-radius: 50%;
    background: radial-gradient(circle at 35% 35%, #fff, #b9bcc1);
  }
  .address {
    position: absolute; left: 52px; bottom: 30px; font-size: 9.5px;
    color: var(--ink); line-height: 1.35; text-align: center;
  }

  /* back A */
  .back-a { background: var(--blue); }
  .back-a__texture {
    position: absolute; inset: 0;
    background: linear-gradient(135deg, #2a8ee0 0%, #1f80d4 50%, #2a8ee0 100%);
  }
  .back-a__brand { position: absolute; left: 0; right: 0; top: 92px; text-align: center; }
  .back-a__mark { font-weight: 700; font-size: 88px; line-height: 1; color: var(--ink); letter-spacing: 4px; }
  .back-a__word { font-size: 14px; letter-spacing: 9px; color: var(--ink); margin-top: 2px; }
  .back-a__url { font-size: 11px; color: var(--ink); margin-top: 4px; }

  /* back B */
  .back-b { background: linear-gradient(160deg, #2a8fe0 0%, var(--blue) 60%, #1a78cc 100%); }
  .back-b__brand { position: absolute; left: 0; right: 0; top: 40px; text-align: center; }
  .back-b__mark { font-weight: 700; font-size: 180px; line-height: 1; color: var(--logo-grey); letter-spacing: 10px; }
  .back-b__word { font-size: 26px; letter-spacing: 16px; color: var(--logo-grey); margin-top: 6px; padding-left: 16px; }
  .back-b__url { font-size: 10px; color: var(--logo-grey); margin-top: 10px; }
</style>
</head>
<body>

  <!-- Row 1: front -->
  <section class="card card--front-a">
    <div class="front__brand"></div>
    <div class="front__detail"></div>
    <div class="front__strip"></div>
    <div class="brand">
      <div class="brand__mark">RW</div>
      <div class="brand__word">FRAMEWORKS</div>
      <div class="brand__url">www.rwframeworkmasonry.com</div>
    </div>
    <div class="social" aria-label="Social profiles">
      <span class="social__chip"></span><span class="social__chip"></span>
      <span class="social__chip"></span><span class="social__chip"></span>
    </div>
    <div style="position:absolute;left:215px;top:0;right:0;height:100%;">
      <div class="person">
        <div class="person__name">DANIEL WHITCOMBE</div>
        <div class="person__role"><span class="person__rule"></span>Owner</div>
      </div>
      <ul class="contacts">
        <li><span class="dot"></span>office@rwframeworks-mail.com</li>
        <li><span class="dot"></span>555-210-4830</li>
        <li><span class="dot"></span>555-384-9172</li>
        <li><span class="dot"></span>whitcombe@ridgeworkdesign.com</li>
      </ul>
      <p class="address">Address: 1420 Quarry Road, Suite 310<br>Millbrook, TX 75000</p>
    </div>
  </section>

  <!-- Row 1: back -->
  <section class="card card--back-a back-a">
    <div class="back-a__texture" role="img" aria-label="Repeating brand-mark pattern in light and mid blue"></div>
    <div class="back-a__brand">
      <div class="back-a__mark">RW</div>
      <div class="back-a__word">FRAMEWORKS</div>
      <div class="back-a__url">www.rwframeworkmasonry.com</div>
    </div>
  </section>

  <!-- Row 2: front -->
  <section class="card card--front-b">
    <div class="front__brand"></div>
    <div class="front__detail"></div>
    <div class="front__strip"></div>
    <div class="brand">
      <div class="brand__mark">RW</div>
      <div class="brand__word">FRAMEWORKS</div>
      <div class="brand__url">www.rwframeworkmasonry.com</div>
    </div>
    <div class="social" aria-label="Social profiles">
      <span class="social__chip"></span><span class="social__chip"></span>
      <span class="social__chip"></span><span class="social__chip"></span>
    </div>
    <div style="position:absolute;left:215px;top:0;right:0;height:100%;">
      <div class="person">
        <div class="person__name">DANIEL WHITCOMBE</div>
        <div class="person__role"><span class="person__rule"></span>Owner</div>
      </div>
      <ul class="contacts">
        <li><span class="dot"></span>office@rwframeworks-mail.com</li>
        <li><span class="dot"></span>555-210-4830</li>
        <li><span class="dot"></span>555-384-9172</li>
        <li><span class="dot"></span>whitcombe@ridgeworkdesign.com</li>
      </ul>
      <p class="address">Address: 1420 Quarry Road, Suite 310<br>Millbrook, TX 75000</p>
    </div>
  </section>

  <!-- Row 2: back -->
  <section class="card card--back-b back-b">
    <div class="back-b__brand">
      <div class="back-b__mark">RW</div>
      <div class="back-b__word">FRAMEWORKS</div>
      <div class="back-b__url">www.rwframeworkmasonry.com</div>
    </div>
  </section>

</body>
</html>
```